Keltby Swimming Club needs a poster to gain new members

We need a poster design to put up on noticeboards etc. to gain new members.
KELTBY SWIMMING CLUB
Outdoor 50m pool
Gold Level (National) Coach - over 30 years experience
Bronze Licence Assistant Coach
Our squads -
State/National (includes Pool, Surf, Triathletes)
Development Squad
Junior Squad (from 8 years of age)
Every member is valued and every swimmer is provided the opportunity to realise their dreams and potential.
Family atmosphere encouraging a healthy mix of social activities and fun.
State Champion Open Water Swimming Club since 2000.
New members welcome - contact Darren Walsh - keltby.coaching@swimpostmail.net or 0417 860 294
(OUR COLOURS ARE NAVY BLUE, LIGHT BLUE AND WHITE SO WOULD LIKE THE COLOUR SCHEME OF THE POSTER TO SUIT).
A PICTURE OF OUR TSHIRT IS SHOWN ONLY AS I WOULD LIKE THE LETTERING OF KELTBY SWIMMING CLUB TO BE SIMILAR ON THE POSTER.
basically the poster needs to be eye catching to get people to stop and read and want to join our club!!!!

```html
<!DOCTYPE html>
<html lang="en">
<head>
<meta charset="utf-8">
<title>Keltby Swimming Club – New Members Poster</title>
<link rel="stylesheet" href="https://fonts.googleapis.com/css2?family=Graduate&family=Nunito+Sans:ital,wght@0,700;0,800;1,700;1,800&display=swap">
<style>
  :root {
    --navy: #0b168a;
    --navy-panel: #2b3d92;
    --royal: #2f5cc8;
    --water-light: #7db4f0;
    --sky: #22a7e8;
    --white: #ffffff;
    --text-navy: #27368c;
  }
  * { margin: 0; padding: 0; box-sizing: border-box; }
  html, body { width: 1200px; height: 1000px; overflow: hidden; background: var(--white); }
  body { position: relative; font-family: "Nunito Sans", Arial, sans-serif; }

  .poster { position: absolute; left: 246px; top: 0; width: 708px; height: 1000px; overflow: hidden; background: var(--water-light); }
  .band { position: absolute; left: 0; width: 100%; }
  .band--top { top: 0; height: 52px; background: linear-gradient(180deg, #081080, var(--navy)); }
  .band--white { background: var(--white); }
  .band--navy { background: var(--navy); }
  .band--sky { background: var(--sky); }
  .band--panel { background: var(--navy-panel); }

  .title-zone { position: absolute; left: 0; top: 82px; width: 100%; height: 198px;
    background: radial-gradient(ellipse at 70% 40%, #4a78d8 0%, var(--royal) 55%, #2a52bb 100%); }
  .water { position: absolute; left: 0; top: 310px; width: 100%; height: 545px;
    background: radial-gradient(ellipse at 80% 30%, #6aa2ea 0%, #4b85dd 35%, #5f9ae6 70%, #84b9f2 100%); }
  .water-foot { position: absolute; left: 0; top: 940px; width: 100%; height: 60px;
    background: linear-gradient(180deg, #6aa6ee, var(--water-light)); }

  .club-name { position: absolute; left: 0; width: 100%; text-align: center; font-family: "Graduate", Georgia, serif; color: var(--white);
    -webkit-text-stroke: 2px var(--sky); paint-order: stroke fill; }
  .club-name__main { top: 94px; font-size: 100px; line-height: 1; letter-spacing: 1px; }
  .club-name__sub { top: 204px; font-size: 52px; line-height: 1; letter-spacing: 3px; }

  .squads-panel { position: absolute; left: 42px; top: 555px; width: 274px; height: 300px; background: var(--navy-panel); }
  .squads-panel__title { position: absolute; left: 20px; top: 72px; font-size: 21px; font-weight: 800; color: var(--white); }
  .rule { position: absolute; height: 8px; border-top: 3px solid var(--white); border-bottom: 3px solid var(--white); }
  .squads-panel .rule { left: 0; top: 106px; width: 274px; }
  .squads-list { position: absolute; left: 22px; top: 132px; list-style: none; color: var(--white); font-size: 15.5px; font-weight: 800; line-height: 19px; }
  .squads-list li { margin-bottom: 16px; }

  .photo-frame { position: absolute; }
  .photo-frame svg { display: block; }

  .features { position: absolute; left: 389px; top: 0; width: 250px; height: 860px; text-align: center; color: var(--white); font-weight: 700; font-size: 18px; line-height: 21.3px; }
  .feature { position: absolute; left: 0; width: 250px; white-space: nowrap; }
  .feature em { font-style: italic; }
  .features .rule { left: 4px; width: 242px; }

  .welcome-badge { position: absolute; left: 274px; top: 756px; }

  .contact { position: absolute; left: 0; top: 872px; width: 100%; height: 50px; background: var(--white);
    display: flex; align-items: center; justify-content: center; gap: 16px; color: var(--text-navy); font-size: 16px; font-weight: 800; }
</style>
</head>
<body>
<main class="poster">
  <div class="band band--top"></div>
  <div class="band band--white" style="top:52px;height:8px"></div>
  <div class="band band--navy" style="top:60px;height:7px"></div>
  <div class="band band--white" style="top:67px;height:15px"></div>

  <div class="title-zone"></div>
  <h1 class="club-name club-name__main">KELTBY</h1>
  <h2 class="club-name club-name__sub">SWIMMING CLUB</h2>

  <div class="band band--white" style="top:280px;height:13px"></div>
  <div class="band" style="top:293px;height:8px;background:#4a73cf"></div>
  <div class="band band--white" style="top:301px;height:9px"></div>

  <div class="water"></div>

  <section class="squads-panel">
    <h3 class="squads-panel__title">OUR SQUADS</h3>
    <div class="rule"></div>
    <ul class="squads-list">
      <li>STATE/NATIONAL (INCLUDES<br>POOL, SURF, TRIATHLETES)</li>
      <li>DEVELOPMENT SQUAD</li>
      <li>JUNIOR SQUAD (FROM<br>8 YEARS OF AGE)</li>
    </ul>
  </section>

  <div class="photo-frame" style="left:-6px;top:266px">
    <svg width="310" height="310" viewBox="0 0 310 310">
      <defs>
        <linearGradient id="teamPhoto" x1="0" y1="0" x2="0" y2="1">
          <stop offset="0" stop-color="#cfd6df"/><stop offset="0.45" stop-color="#2a3550"/><stop offset="0.8" stop-color="#1e2840"/><stop offset="1" stop-color="#e9ecef"/>
        </linearGradient>
      </defs>
      <circle cx="155" cy="155" r="152" fill="var(--navy-panel)"/>
      <circle cx="155" cy="155" r="141" fill="var(--sky)"/>
      <circle cx="155" cy="155" r="136" fill="url(#teamPhoto)" role="img" aria-label="Club swimmers in navy team shirts gathered behind a sponsors banner"/>
    </svg>
  </div>

  <div class="photo-frame" style="left:178px;top:470px">
    <svg width="190" height="190" viewBox="0 0 190 190">
      <defs>
        <linearGradient id="poolPhoto" x1="0" y1="0" x2="0" y2="1">
          <stop offset="0" stop-color="#4b8fe0"/><stop offset="0.4" stop-color="#7fb0d8"/><stop offset="0.65" stop-color="#2fb0d9"/><stop offset="1" stop-color="#c9a98a"/>
        </linearGradient>
      </defs>
      <circle cx="95" cy="95" r="93" fill="var(--navy-panel)"/>
      <circle cx="95" cy="95" r="84" fill="var(--sky)"/>
      <circle cx="95" cy="95" r="79" fill="url(#poolPhoto)" role="img" aria-label="Outdoor 50 metre pool with starting blocks under a blue sky"/>
    </svg>
  </div>

  <section class="features">
    <p class="feature" style="top:325px">OUTDOOR 50M POOL</p>
    <div class="rule" style="top:349px"></div>
    <p class="feature" style="top:362px">GOLD LEVEL<br>(NATIONAL) COACH<br><em>30 YEARS EXPERIENCE</em></p>
    <div class="rule" style="top:430px"></div>
    <p class="feature" style="top:447px">BRONZE LICENCE<br>ASSISTANT COACH</p>
    <div class="rule" style="top:499px"></div>
    <p class="feature" style="top:517px">STATE CHAMPION OPEN<br>WATER SWIMMING<br>CLUB SINCE 2000</p>
    <div class="rule" style="top:590px"></div>
    <p class="feature" style="top:610px">FAMILY ATMOSPHERE<br>ENCOURAGING A<br>HEALTHY MIX OF SOCIAL<br>ACTIVITIES AND FUN</p>
    <div class="rule" style="top:703px"></div>
    <p class="feature" style="top:718px">EVERY MEMBER IS<br>VALUED AND EVERY<br>SWIMMER IS PROVIDED<br>THE OPPORTUNITY TO<br>REALISE THEIR DREAMS<br>AND POTENTIAL</p>
  </section>

  <div class="band band--panel" style="top:855px;height:10px"></div>
  <div class="band band--sky" style="top:865px;height:7px"></div>
  <footer class="contact">
    <span>CONTACT DARREN</span><span>|</span><span>0417 860 294</span><span>|</span><span>KELTBY.COACHING@SWIMPOSTMAIL.NET</span>
  </footer>
  <div class="band band--sky" style="top:922px;height:8px"></div>
  <div class="band band--panel" style="top:930px;height:10px"></div>
  <div class="water-foot"></div>

  <svg class="welcome-badge" width="124" height="124" viewBox="0 0 124 124">
    <circle cx="62" cy="62" r="61" fill="var(--navy-panel)"/>
    <circle cx="62" cy="62" r="54" fill="var(--sky)"/>
    <circle cx="62" cy="62" r="49" fill="var(--white)"/>
    <g font-family="Nunito Sans, Arial, sans-serif" font-weight="800" font-size="15" fill="var(--text-navy)" text-anchor="middle">
      <text x="62" y="47">NEW</text>
      <text x="62" y="66">MEMBERS</text>
      <text x="62" y="85">WELCOME</text>
    </g>
  </svg>
</main>
</body>
</html>
```